Design a Flyer for our Domestic Cleaning Promotion

We are full on company doing commercial & industrial cleaning. We are planning to hit domestic sector too. That's why we need a flyer for promotion.

It has to be creative and catchy!

Logo is attached.

Target: Sidney metro areas & suburbs domestic/ residential blocks

size: A6 Both sides horizontal

Front side: Promotion "100$ 4 hours first off, regular domestic cleaning." (usually we charge 100$ for 3 hours of cleaning) Conditions apply. We prefer to put an image of "living area" or "living room", regular cozy. On top of it, you play with any other vector. You can promote 100$ for 4 hours cleaning or 25$ per hour... anything suites design.

For catchy slogan, google it or check it from http://lnkvx.io/kTr8Wm or http://lnkvx.io/Qz4NhY You get the idea!

Back side: 3 blocks of promotions. 1. Domestic. 2. Commercial 3. Industrial
may be you can put some bullets, I am not sure! Shoot something creative! Check the sample here http://img.pixorra.net/mH3sLq9.jpg
So, 3 blocks, 3 background images (1. Domestic 2. Commercial/ offices 3. Industrial) google images for "Industrial cleaning" or "commercial cleaning" so you understand what kind of images can fit there. Each image blocks, there will be few bullets, where we can put few words.
Suppose, we can say, "WE ARE OFFERING..." big. Then 3 images, and few bullets on each images. phone number and website at the bottom.

Lets just put our phone number as +4187302615 & website: brightnook.com.au

```html
<!DOCTYPE html>
<html lang="en">
<head>
<meta charset="utf-8">
<title>Tidora – Regular Domestic Cleaning</title>
<link rel="stylesheet" href="https://fonts.googleapis.com/css2?family=Archivo+Black&family=Arimo:ital,wght@0,700;1,700&display=swap">
<style>
  :root {
    --ink: #3a2e28;
    --logo-ink: #3c3c3c;
    --orange: #e8622a;
    --green: #8cc63f;
    --white: #ffffff;
    --wall: #ecebea;
    --room-light: #f3efe9;
    --room-mid: #d9d2c8;
    --room-dark: #a89b8c;
  }
  * { margin: 0; padding: 0; box-sizing: border-box; }
  html, body { width: 1200px; height: 851px; overflow: hidden; background: var(--white); }
  .flyer {
    position: relative;
    width: 1200px;
    height: 851px;
    overflow: hidden;
    background: var(--wall);
    font-family: "Arimo", Arial, sans-serif;
  }
  .room-photo {
    position: absolute;
    left: 0; top: 0;
    width: 1200px; height: 553px;
    background:
      linear-gradient(180deg, rgba(255,255,255,0) 60%, rgba(168,155,140,0.55) 100%),
      linear-gradient(90deg, var(--room-mid) 0%, var(--room-light) 35%, var(--room-light) 65%, var(--room-mid) 100%);
  }
  .brand {
    position: absolute;
    left: 755px; top: 32px;
    display: flex;
    align-items: center;
    gap: 22px;
  }
  .brand-mark {
    width: 96px; height: 96px;
    border-radius: 50%;
    background: var(--green);
  }
  .brand-name {
    font-weight: 700;
    font-size: 72px;
    color: var(--logo-ink);
    letter-spacing: -1px;
  }
  .headline-panel {
    position: absolute;
    left: 229px; top: 211px;
    width: 735px; height: 249px;
    background: rgba(255,255,255,0.55);
  }
  .headline {
    position: absolute;
    left: 254px; top: 238px;
    width: 676px;
    font-family: "Archivo Black", "Arial Black", sans-serif;
    font-weight: 400;
    color: var(--ink);
    line-height: 1;
  }
  .headline-top {
    display: flex;
    align-items: baseline;
    justify-content: space-between;
    font-size: 76px;
    height: 100px;
  }
  .headline-top .initial { font-size: 110px; }
  .headline-bottom {
    display: block;
    margin-top: 14px;
    font-size: 88px;
    letter-spacing: 1px;
    white-space: nowrap;
    text-align: center;
  }
  .headline-rule {
    position: absolute;
    left: 254px; top: 469px;
    width: 690px; height: 7px;
    background: var(--orange);
  }
  .service-label {
    position: absolute;
    left: 131px;
    background: var(--orange);
    color: var(--white);
    font-weight: 700;
    font-size: 47px;
    height: 56px;
    line-height: 56px;
    padding: 0 12px;
    letter-spacing: 1.5px;
    white-space: nowrap;
  }
  .service-label.line-1 { top: 616px; width: 558px; }
  .service-label.line-2 { top: 689px; width: 280px; height: 54px; line-height: 54px; }
  .offer-ribbon {
    position: absolute;
    left: 869px; top: 556px;
    width: 203px; height: 248px;
  }
  .offer-text {
    position: absolute;
    left: 869px; top: 570px;
    width: 203px;
    text-align: center;
    color: var(--white);
    font-weight: 700;
    font-size: 33px;
    line-height: 43px;
  }
  .offer-text .price { display: block; margin-bottom: 8px; }
  .terms {
    position: absolute;
    left: 27px; top: 800px;
    font-style: italic;
    font-weight: 700;
    font-size: 16px;
    font-variant: small-caps;
    color: var(--ink);
  }
</style>
</head>
<body>
  <main class="flyer">
    <div class="room-photo" role="img" aria-label="Bright, cosy living room with white sofas, fireplace, wooden coffee table and plants"></div>

    <div class="brand">
      <span class="brand-mark"></span>
      <span class="brand-name">Tidora</span>
    </div>

    <div class="headline-panel"></div>
    <h1 class="headline">
      <span class="headline-top"><span class="initial">C</span><span>L</span><span>E</span><span>A</span><span>N</span><span>I</span><span>N</span><span>G</span></span>
      <span class="headline-bottom">AT ITS FINEST</span>
    </h1>
    <div class="headline-rule"></div>

    <p class="service-label line-1">REGULAR DOMESTIC</p>
    <p class="service-label line-2">CLEANING</p>

    <svg class="offer-ribbon" viewBox="0 0 203 248" aria-hidden="true">
      <polygon points="0,0 203,0 203,248 101.5,190 0,248" fill="var(--green)"/>
      <polygon points="10,8 193,8 193,230 101.5,179 10,230" fill="none" stroke="var(--white)" stroke-width="2" stroke-dasharray="7 5"/>
    </svg>
    <p class="offer-text"><span class="price">100$</span>4 HOURS<br>FIRST OFF</p>

    <p class="terms">*Terms &amp; conditions apply</p>
  </main>
</body>
</html>
```